Roofing Company Modern look

I want a modern and sophisticated look for our roofing business.

Our address is :

5172 Maple Crane Rd
Orlando, Fl 32825

(407)-555-2719

www.SummitPeakRoofs.example

I also want to make sure on the back there is a spot to put
Project Manager Name :

Number:

Because the cards will be used by all sales people

Project Manager Name :

Also there are accreditation we have logos are uploaded here as well that I would like maybe on the back of card as well

I also want to highlight our special attributions or trades:

Residential & Commercial
Fully Insured
License # CCC8274916
Insurance Claims
Serving Central Florida Since 1992
Free Estimates

Contact Information for Business Card

Our address is :

5172 Maple Crane Rd
Orlando, Fl 32825

(407)-555-2719

Project Manager Name :

Residential & Commercial
Fully Insured
License # CCC8274916
Insurance Claims
Free Estimates

Font styles to use
Serif
Sans Serif

Colors
3176b5

Requirements
Must have
• Must have royal blue like my logo grey and black are the colors I like

```html
<!DOCTYPE html>
<html lang="en">
<head>
<meta charset="utf-8">
<title>Summit Peak Roofing &amp; Gutters – Business Card</title>
<link href="https://fonts.googleapis.com/css2?family=Lato:wght@400;700&family=Montserrat:wght@500;600&display=swap" rel="stylesheet">
<style>
  :root {
    --stage: #2b2b2b;
    --card-dark: #222324;
    --card-black: #0a0a0a;
    --paper-soft: #f3f4f6;
    --royal: #3176b5;
    --royal-deep: #1b57a0;
    --sky: #2ea6e0;
    --text-light: #f2f2f2;
    --slot: #c9ced6;
  }
  * { box-sizing: border-box; margin: 0; padding: 0; }
  html, body { width: 1200px; height: 1192px; overflow: hidden; }
  body { background: var(--stage); position: relative; font-family: "Lato", sans-serif; }

  .card {
    position: absolute; left: 209px; width: 782px; height: 448px;
    border-radius: 14px; overflow: hidden;
    box-shadow: 0 8px 20px rgba(0,0,0,.45);
  }
  .card-front { top: 130px; background: var(--card-dark); }
  .card-back { top: 614px; background: var(--card-black); }

  .front-shape { position: absolute; inset: 0; }

  .front-brand {
    position: absolute; left: 40px; top: 190px; width: 330px;
    text-align: center; color: var(--royal);
    font-family: "Montserrat", sans-serif; font-weight: 600;
    line-height: 1.2;
  }
  .front-brand .brand-main { display: block; font-size: 38px; letter-spacing: 3px; }
  .front-brand .brand-sub { display: block; font-size: 14px; letter-spacing: 2.5px; margin-top: 4px; }

  .contact {
    position: absolute; right: 52px; top: 54px; text-align: right;
    color: var(--text-light); font-size: 19px; line-height: 23px;
  }
  .person-name { font-size: 26px; font-weight: 700; line-height: 30px; }
  .person-name .surname { color: var(--royal); margin-left: 6px; }
  .person-role { margin-bottom: 34px; }
  .accent { color: var(--sky); }
  .block { margin-bottom: 24px; }
  .contact-lines { margin-right: 22px; }
  .contact-line { display: flex; justify-content: flex-end; align-items: center; gap: 10px; }
  .contact-line svg { width: 14px; height: 14px; flex: none; margin-right: -22px; }

  .feature-band {
    position: absolute; left: 0; right: 0; top: 368px; height: 29px;
    background: linear-gradient(90deg, var(--royal-deep) 0%, var(--royal) 45%, var(--sky) 100%);
    display: flex; align-items: center; justify-content: flex-end;
    padding-right: 52px; gap: 9px;
    color: #fff; font-size: 17.5px;
  }
  .feature-band .dot { width: 7px; height: 7px; border-radius: 50%; background: #111; }

  .back-brand {
    position: absolute; left: 0; right: 0; top: 128px; text-align: center;
    color: var(--royal); font-family: "Montserrat", sans-serif; font-weight: 600;
    line-height: 1.15;
  }
  .back-brand .brand-main { display: block; font-size: 46px; letter-spacing: 4px; }
  .back-brand .brand-sub { display: block; font-size: 19px; letter-spacing: 2px; margin-top: 4px; }

  .back-web {
    position: absolute; left: 0; right: 0; top: 289px; text-align: center;
    color: #fff; font-family: "Montserrat", sans-serif; font-weight: 500;
    font-size: 20px; letter-spacing: 1.5px;
  }
  .partners {
    position: absolute; left: 0; right: 0; top: 332px; bottom: 0;
    background: var(--paper-soft); border-top: 3px solid var(--royal);
  }
  .partners-title {
    position: absolute; left: 50%; top: -14px; transform: translateX(-50%);
    background: var(--royal); color: #fff; border-radius: 12px;
    padding: 0 10px; height: 24px; line-height: 24px; white-space: nowrap;
    font-family: "Montserrat", sans-serif; font-weight: 500; font-size: 19px; letter-spacing: .5px;
  }
  .badge-row {
    position: absolute; left: 0; right: 0; top: 30px;
    display: flex; justify-content: center; gap: 38px;
  }
  .badge-slot {
    width: 92px; height: 62px; border-radius: 6px; background: var(--slot);
  }
</style>
</head>
<body>

<section class="card card-front">
  <svg class="front-shape" viewBox="0 0 782 448" width="782" height="448" aria-hidden="true">
    <defs>
      <linearGradient id="curveBlue" x1="0" y1="0" x2="0" y2="1">
        <stop offset="0" stop-color="#2ea6e0"/>
        <stop offset="1" stop-color="#1b3f8a"/>
      </linearGradient>
    </defs>
    <path d="M0 0 H305 C370 90 402 200 402 268 C402 340 365 400 341 448 H0 Z" fill="url(#curveBlue)"/>
    <path d="M0 0 H305 C360 90 388 200 386 268 C384 340 345 400 318 448 H0 Z" fill="#ffffff"/>
  </svg>

  <div class="front-brand">
    <span class="brand-main">SUMMIT PEAK</span>
    <span class="brand-sub">ROOFING &amp; GUTTERS INC.</span>
  </div>

  <div class="contact">
    <div class="person-name">DANIEL<span class="surname">MARSH</span></div>
    <div class="person-role">Project Manager</div>
    <div class="block"><span class="accent">License #</span> CCC8274916<br>Residential &amp; Commercial</div>
    <div class="block">5172 Maple Crane Rd<br>Orlando, Fl 32825</div>
    <div class="contact-lines">
      <div class="contact-line">(407)-555-2719
        <svg viewBox="0 0 16 16" aria-hidden="true"><path fill="#2e86d0" d="M3.5 1.5l2.5 3-1.5 1.6c.8 1.9 2.4 3.5 4.3 4.3l1.6-1.5 3 2.5-1.4 2.4C7.5 13.5 2.5 8.5 1.2 2.9z"/></svg>
      </div>
      <div class="contact-line">SummitPeakRoofs@example.com
        <svg viewBox="0 0 16 16" aria-hidden="true"><rect x="1" y="3" width="14" height="10" rx="1" fill="#2e86d0"/><path d="M1.5 3.5 8 9l6.5-5.5" stroke="#222324" stroke-width="1.3" fill="none"/></svg>
      </div>
      <div class="contact-line">www.SummitPeakRoofs.example
        <svg viewBox="0 0 16 16" aria-hidden="true"><circle cx="8" cy="8" r="7" fill="#2e86d0"/><path d="M5 4c2 1 1 3 3 3s1 3 0 4M10 3c-1 2 1 2 2 3" stroke="#222324" stroke-width="1.2" fill="none"/></svg>
      </div>
    </div>
  </div>

  <div class="feature-band">
    <span>Fully Insured</span><span class="dot"></span>
    <span>Insurance Claims</span><span class="dot"></span>
    <span>Serving Central Florida Since 1992</span><span class="dot"></span>
    <span>Free Estimates</span>
  </div>
</section>

<section class="card card-back">
  <div class="back-brand">
    <span class="brand-main">SUMMIT PEAK</span>
    <span class="brand-sub">ROOFING &amp; GUTTERS LLC.</span>
  </div>
  <div class="back-web">www.summitpeakroofs.example</div>

  <div class="partners">
    <div class="partners-title">Our Accreditations &amp; Partners</div>
    <div class="badge-row">
      <div class="badge-slot" role="img" aria-label="Accreditation badge"></div>
      <div class="badge-slot" role="img" aria-label="Manufacturer certification badge"></div>
      <div class="badge-slot" role="img" aria-label="Authorized contractor badge"></div>
      <div class="badge-slot" role="img" aria-label="Approved listing badge"></div>
    </div>
  </div>
</section>

</body>
</html>
```